Investment company seeks website design

TBW (Tallowbrook Wealth Partners) are an investment company that actively targets and acquires businesses and grows them after acquisition.

The website design needs to be professional and should communicate to key decision-makers inside the acquirable companies that TBW targets.

You will design the Homepage initially for the competition. If you win the competition, you will design the inner pages too.

More details are attached below.

Target Market(s)

Business owners and decision makers inside acquirable companies

Industry/Entity Type

Company Investment

Number of Pages Required

5+ page

Requirements
Must have
• High Attention to Detail. Following the Wireframes closely. Consistent colour and design choices
Should not have
• Anything cheap, too bright or untidy

```html
<!DOCTYPE html>
<html lang="en">
<head>
<meta charset="utf-8">
<title>Tallowbrook Wealth Partners – Home</title>
<link href="https://fonts.googleapis.com/css2?family=Poppins:wght@400;500;600;700&display=swap" rel="stylesheet">
<style>
:root{
  --navy:#13284f;
  --navy-deep:#0f2347;
  --green:#6bb33f;
  --green-soft:#eef5e8;
  --blue:#1b56a8;
  --grey-bg:#eef0ee;
  --text:#3a4660;
  --muted:#8a93a3;
  --white:#ffffff;
}
*{box-sizing:border-box;margin:0;padding:0}
html,body{width:1200px;height:4412px;overflow:hidden}
body{font-family:'Poppins',sans-serif;color:var(--navy);background:var(--white);position:relative}
.abs{position:absolute}
.btn{position:absolute;display:flex;align-items:center;justify-content:center;font-size:11px;font-weight:600;color:var(--white);border-radius:2px;white-space:nowrap}
.btn-green{background:var(--green)}
.btn-navy{background:var(--navy)}
.section{position:absolute;left:0;width:1200px}

/* nav */
.nav{top:0;height:64px;background:var(--white);box-shadow:0 2px 6px rgba(0,0,0,.05)}
.brand{position:absolute;display:flex;align-items:center;gap:10px}
.brand-mark{width:30px;height:30px;background:var(--navy);border-radius:3px}
.brand-name{font-weight:500;letter-spacing:1px;color:var(--navy)}
.nav-links{position:absolute;left:497px;top:0;height:64px;display:flex;align-items:center;gap:40px;font-size:11px;font-weight:500;color:var(--navy)}
.nav-links .active{border-bottom:2px solid var(--green);padding-bottom:4px}

/* hero */
.hero{top:64px;height:499px;overflow:hidden}
.hero-photo{position:absolute;inset:0;background:linear-gradient(135deg,#4a5f86 0%,#3d5177 45%,#56698f 75%,#334468 100%)}
.hero-photo::after{content:"";position:absolute;inset:0;background:rgba(27,45,90,.35)}
.hero-title{position:absolute;width:420px;margin-left:-210px;color:var(--white);font-weight:700;font-size:37px;line-height:44px;text-align:center;display:flex;flex-direction:column;align-items:center;white-space:nowrap}
.hero-title .ghost{color:rgba(255,255,255,.35)}
.hero-divider{position:absolute;left:598px;top:110px;width:2px;height:280px;background:rgba(255,255,255,.35)}

/* thrive */
.thrive{top:563px;height:583px;background:var(--green-soft)}
.thrive-frame{position:absolute;left:272px;top:72px;width:280px;height:400px;border:2px solid var(--green)}
.thrive-photo{position:absolute;left:199px;top:92px;width:331px;height:414px;background:linear-gradient(180deg,#f3b36a 0%,#c9a58a 30%,#7a8aa3 65%,#3d4a5e 100%)}
.h2{font-weight:700;color:var(--navy)}
.thrive-copy{position:absolute;left:642px;top:128px;width:380px}
.thrive-copy h2{font-size:28px;line-height:32px}
.small{font-size:9px;line-height:15px;color:var(--text)}
.services-title{font-size:12px;font-weight:600;margin-top:22px}
.ticks{list-style:none;margin-top:10px}
.ticks li{display:flex;align-items:center;gap:8px;font-size:9.5px;line-height:19px;color:var(--text)}
.ticks svg{flex:none}

/* qualities */
.qualities{top:1146px;height:828px;background:var(--white)}
.center-title{position:absolute;left:0;width:1200px;text-align:center;font-weight:600;color:var(--navy)}
.quality{position:absolute;width:480px;height:260px}
.quality svg{position:absolute;left:0;top:0}
.quality-text{position:absolute;left:208px;top:76px;width:270px}
.quality-text h3{font-size:14px;font-weight:600;margin-bottom:8px}
.quality-text ul{padding-left:12px;font-size:8.5px;line-height:14px;color:var(--text)}
.readmore{font-size:8.5px;color:var(--green);font-weight:500;margin-top:10px;display:block}

/* explore */
.explore{top:1974px;height:283px;background:linear-gradient(120deg,#1d5bb0 0%,#164e9c 55%,#1a56a8 100%)}
.explore h2{position:absolute;left:0;width:1200px;top:60px;text-align:center;color:var(--white);font-size:36px;font-weight:600}
.explore p{position:absolute;left:200px;width:800px;top:133px;text-align:center;color:#dbe6f6;font-size:15px;line-height:22px}

/* transform */
.transform{top:2257px;height:620px;background:var(--green-soft)}
.step{position:absolute;width:241px;height:278px}
.step svg.hex{position:absolute;left:0;top:0}
.step-body{position:absolute;left:30px;top:70px;width:181px;text-align:center}
.step-body h4{font-size:13px;font-weight:600;line-height:15px;margin-top:12px}
.step-body p{font-size:9px;line-height:13px;margin-top:10px}
.step.faded .step-body{color:#a9b0ba}
.step.green .step-body{color:var(--green)}

/* news */
.news{top:2877px;height:657px;background:var(--white)}
.card{position:absolute;top:139px;width:250px;height:374px;background:var(--white);box-shadow:0 2px 10px rgba(0,0,0,.08);text-align:center}
.card-photo{height:184px}
.card-date{font-size:9px;color:var(--green);margin-top:8px}
.card h4{font-size:12px;font-weight:600;line-height:16px;margin:8px 20px 0}
.card p{font-size:8.5px;line-height:14px;color:var(--text);margin:10px 34px 0}
.card .readmore{margin-top:14px}
.arrow{position:absolute;top:224px}

/* balance */
.balance{top:3534px;height:618px;background:var(--grey-bg)}
.balance h2{position:absolute;left:0;width:1200px;text-align:center;font-size:26px;font-weight:600;line-height:37px}

/* footer */
.footer{top:4152px;height:260px;background:var(--navy-deep);color:var(--white)}
.f-col{position:absolute;top:70px}
.f-col h5{font-size:11px;font-weight:500;color:var(--green);margin-bottom:14px}
.f-col a{display:block;font-size:10px;line-height:22px;color:#d9e0ec;text-decoration:none}
.f-bottom{position:absolute;left:199px;right:199px;top:206px;border-top:1px solid rgba(255,255,255,.15);padding-top:14px;display:flex;justify-content:space-between;align-items:center;font-size:8.5px;color:#aab4c7}
.socials{display:flex;gap:10px}
.socials i{width:20px;height:20px;border-radius:50%;background:#5f6f8c;display:block}
</style>
</head>
<body>

<header class="section nav">
  <div class="brand" style="left:103px;top:17px">
    <span class="brand-mark"></span>
    <span class="brand-name" style="font-size:14px">TALLOWBROOK</span>
  </div>
  <nav class="nav-links">
    <span class="active">Home</span>
    <span>Our Approach</span>
    <span>Investment Criteria</span>
    <span>About Us</span>
    <span>Contact Us</span>
  </nav>
  <a class="btn btn-green" style="left:992px;top:17px;width:88px;height:30px">✉&nbsp; Email Us</a>
</header>

<section class="section hero">
  <div class="hero-photo" role="img" aria-label="Photo of three business people cheering with raised arms in front of a glass office building"></div>
  <div class="hero-divider"></div>
  <div class="hero-title" style="left:330px;top:180px">
    <span>The Best Exit</span><span class="ghost">for You</span>
  </div>
  <div class="hero-title" style="left:904px;top:176px">
    <span>The Best Future for</span><span class="ghost">Your Business</span>
  </div>
  <a class="btn btn-green" style="left:548px;top:393px;width:100px;height:30px">Discover TBW</a>
</section>

<section class="section thrive">
  <div class="thrive-frame"></div>
  <div class="thrive-photo" role="img" aria-label="Photo of a businessman climbing steps toward a sunlit city skyline"></div>
  <div class="thrive-copy">
    <h2 class="h2">We will make your<br>business thrive</h2>
    <p class="small" style="margin-top:18px;width:350px">TBW is committed to helping businesses achieve significant growth. Under our stewardship, companies have the benefit of an experienced team expert in operations and financing to ensure that every company achieves their full potential.</p>
    <p class="services-title">Our Services Include:</p>
    <ul class="ticks">
      <li><svg width="12" height="10" viewBox="0 0 12 10"><path d="M1 5l3 3 7-7" fill="none" stroke="#6bb33f" stroke-width="2"/></svg>Crafting long-term growth</li>
      <li><svg width="12" height="10" viewBox="0 0 12 10"><path d="M1 5l3 3 7-7" fill="none" stroke="#6bb33f" stroke-width="2"/></svg>Streamlining operations for maximum efficiency</li>
      <li><svg width="12" height="10" viewBox="0 0 12 10"><path d="M1 5l3 3 7-7" fill="none" stroke="#6bb33f" stroke-width="2"/></svg>Providing expert advice to improve management decisions</li>
      <li><svg width="12" height="10" viewBox="0 0 12 10"><path d="M1 5l3 3 7-7" fill="none" stroke="#6bb33f" stroke-width="2"/></svg>Optimising financial structures for expansion</li>
      <li><svg width="12" height="10" viewBox="0 0 12 10"><path d="M1 5l3 3 7-7" fill="none" stroke="#6bb33f" stroke-width="2"/></svg>Facilitating strategic mergers and acquisitions</li>
    </ul>
  </div>
  <a class="btn btn-navy" style="left:822px;top:447px;width:146px;height:30px">Unlock Your Potential</a>
</section>

<section class="section qualities">
  <h2 class="center-title" style="top:72px;font-size:28px">Our qualities &amp; capabilities</h2>

  <div class="quality" style="left:103px;top:136px">
    <svg width="206" height="258" viewBox="0 0 206 258"><defs><linearGradient id="qa" x1="0" y1="0" x2="1" y2="1"><stop offset="0" stop-color="#e9e4dc"/><stop offset=".5" stop-color="#d88a4a"/><stop offset="1" stop-color="#5a4a3c"/></linearGradient></defs><polygon role="img" aria-label="Photo of a hand with a pen beside colourful cone chart pieces" points="103,0 206,64 206,194 103,258 0,194 0,64" fill="url(#qa)"/></svg>
    <div class="quality-text"><h3>Driving value</h3><ul><li>Comprehensive long-term plan</li><li>Ownership of company performance</li><li>Vast experience in driving transformation</li></ul><span class="readmore">Read More ↗</span></div>
  </div>

  <div class="quality" style="left:611px;top:136px">
    <svg width="206" height="258" viewBox="0 0 206 258"><defs><linearGradient id="qb" x1="0" y1="0" x2="1" y2="1"><stop offset="0" stop-color="#c9ced6"/><stop offset=".5" stop-color="#7f8797"/><stop offset="1" stop-color="#3d4452"/></linearGradient></defs><polygon role="img" aria-label="Photo of a team working together at laptops in an office" points="103,0 206,64 206,194 103,258 0,194 0,64" fill="url(#qb)"/></svg>
    <div class="quality-text"><h3>Integrated team</h3><ul><li>Partnership culture</li><li>Consistent senior team</li><li>Detailed industry and operating experience</li></ul><span class="readmore">Read More ↗</span></div>
  </div>

  <div class="quality" style="left:103px;top:420px">
    <svg width="206" height="258" viewBox="0 0 206 258"><defs><linearGradient id="qc" x1="0" y1="0" x2="1" y2="1"><stop offset="0" stop-color="#d6d6d6"/><stop offset=".5" stop-color="#8a8a8a"/><stop offset="1" stop-color="#2f2f33"/></linearGradient></defs><polygon role="img" aria-label="Photo of business partners shaking hands" points="103,0 206,64 206,194 103,258 0,194 0,64" fill="url(#qc)"/></svg>
    <div class="quality-text"><h3>Partnership with management</h3><ul><li>Strong, trust-based relationships</li><li>Significant commitment of time on-the-ground</li><li>Ability to take interim roles if needed</li></ul><span class="readmore">Read More ↗</span></div>
  </div>

  <div class="quality" style="left:611px;top:420px">
    <svg width="206" height="258" viewBox="0 0 206 258"><defs><linearGradient id="qd" x1="0" y1="0" x2="1" y2="1"><stop offset="0" stop-color="#f1f3f7"/><stop offset=".5" stop-color="#a9bfe0"/><stop offset="1" stop-color="#6c7a94"/></linearGradient></defs><polygon role="img" aria-label="Photo of printed financial charts with sticky notes" points="103,0 206,64 206,194 103,258 0,194 0,64" fill="url(#qd)"/></svg>
    <div class="quality-text"><h3>Accelerated execution</h3><ul><li>Relentless focus on priorities</li><li>Drive through to results</li><li>Committed to continuous development</li></ul><span class="readmore">Read More ↗</span></div>
  </div>

  <a class="btn btn-navy" style="left:527px;top:740px;width:146px;height:30px">Contact Us Today!</a>
</section>

<section class="section explore" role="region" aria-label="Explore your next move">
  <h2>Explore your next move</h2>
  <p>If you are looking for a change, then TBW can help you map out a smooth transition, and<br>give you the confidence that your company is in safe hands.</p>
  <a class="btn btn-green" style="left:532px;top:200px;width:136px;height:28px">Discuss with TBW</a>
</section>

<section class="section transform">
  <h2 class="center-title" style="top:90px;font-size:26px;line-height:32px">How tbw will transform<br>your company</h2>

  <div class="step" style="left:200px;top:125px">
    <svg class="hex" width="241" height="278" viewBox="0 0 241 278"><polygon points="120.5,2 239,70 239,208 120.5,276 2,208 2,70" fill="none" stroke="#7d8796" stroke-width="1.5"/></svg>
    <div class="step-body">
      <svg width="46" height="40" viewBox="0 0 46 40" fill="none" stroke="#13284f" stroke-width="2"><path d="M4 38V24h6v14M14 38V18h6v20M24 38V12h6v26M34 38V6h6v32M2 38h42"/><path d="M6 16l10-8 8 4 14-10" stroke="#6bb33f"/></svg>
      <h4>Discover growth<br>opportunities</h4>
      <p>Identify hidden growth opportunities for your business</p>
    </div>
  </div>

  <div class="step faded" style="left:478px;top:186px">
    <svg class="hex" width="241" height="278" viewBox="0 0 241 278"><polygon points="120.5,2 239,70 239,208 120.5,276 2,208 2,70" fill="none" stroke="#c3c9cf" stroke-width="1.5"/></svg>
    <div class="step-body">
      <svg width="46" height="40" viewBox="0 0 46 40" fill="none" stroke="#b4bac2" stroke-width="2"><circle cx="20" cy="18" r="12"/><path d="M14 38l4-8M26 38l-4-8M32 6l8-4M36 12h8"/></svg>
      <h4>Craft strategic<br>solutions</h4>
      <p>Develop precise, results-driven strategies to drive your company forward</p>
    </div>
  </div>

  <div class="step green" style="left:756px;top:125px">
    <svg class="hex" width="241" height="278" viewBox="0 0 241 278"><polygon points="120.5,2 239,70 239,208 120.5,276 2,208 2,70" fill="none" stroke="#a9d38e" stroke-width="1.5"/></svg>
    <div class="step-body">
      <svg width="46" height="40" viewBox="0 0 46 40" fill="none" stroke="#6bb33f" stroke-width="2"><rect x="8" y="4" width="30" height="34" rx="2"/><path d="M14 32l6-8 6 4 8-12"/><path d="M18 10h10"/></svg>
      <h4>Drive future<br>success</h4>
      <p>Lead your company through transformative processes to achieve tangible success</p>
    </div>
  </div>

  <a class="btn btn-green" style="left:527px;top:512px;width:146px;height:30px">Contact Us Today!</a>
</section>

<section class="section news">
  <h2 class="center-title" style="top:70px;font-size:28px">TBW news &amp; insights</h2>
  <svg class="arrow" style="left:156px" width="14" height="20" viewBox="0 0 14 20"><path d="M10 3L4 10l6 7" fill="none" stroke="#13284f" stroke-width="2"/></svg>
  <svg class="arrow" style="left:1030px" width="14" height="20" viewBox="0 0 14 20"><path d="M4 3l6 7-6 7" fill="none" stroke="#13284f" stroke-width="2"/></svg>

  <article class="card" style="left:199px">
    <div class="card-photo" role="img" aria-label="Photo of hands typing on a laptop showing a dashboard" style="background:linear-gradient(135deg,#e8edf2,#9ab7cf 55%,#c89a78)"></div>
    <p class="card-date">02/04/23</p>
    <h4>Lorem ipsum simply dummy printing typesetting</h4>
    <p>It is a long established fact that a reader will be distracted by the readable content of a page when looking at its layout.</p>
    <span class="readmore">Read More ↗</span>
  </article>
  <article class="card" style="left:475px">
    <div class="card-photo" role="img" aria-label="Photo of a businesswoman celebrating in front of city towers" style="background:linear-gradient(135deg,#f7e7b5,#cdd5dd 50%,#5f6f86)"></div>
    <p class="card-date">08/08/23</p>
    <h4>Lorem ipsum simply dummy printing typesetting</h4>
    <p>It is a long established fact that a reader will be distracted by the readable content of a page when looking at its layout.</p>
    <span class="readmore">Read More ↗</span>
  </article>
  <article class="card" style="left:751px">
    <div class="card-photo" role="img" aria-label="Photo of business people shaking hands in a meeting" style="background:linear-gradient(135deg,#d7d2cc,#8b8378 50%,#3a3733)"></div>
    <p class="card-date">15/02/24</p>
    <h4>Lorem ipsum simply dummy printing typesetting</h4>
    <p>It is a long established fact that a reader will be distracted by the readable content of a page when looking at its layout.</p>
    <span class="readmore">Read More ↗</span>
  </article>

  <a class="btn btn-navy" style="left:555px;top:552px;width:90px;height:30px">View All</a>
</section>

<section class="section balance">
  <h2 style="top:72px"><span style="color:var(--green)">Tallowbrook wealth partners:</span><br>Providing balance and growth to your business</h2>

  <svg class="abs" style="left:0;top:0" width="1200" height="618" viewBox="0 0 1200 618">
    <g fill="none" stroke="#6bb33f" stroke-width="1.5">
      <path d="M466 287h24l30 40M733 287h-24l-30 40M466 441h24l30-40M733 441h-24l-30-40"/>
      <polygon points="598,212 725,285 725,440 598,513 471,440 471,285" stroke="#a9d38e"/>
      <polygon points="598,244 697,301 697,424 598,481 499,424 499,301" stroke="#cfe5c0" fill="#ffffff"/>
    </g>
    <text x="598" y="375" text-anchor="middle" font-family="Poppins, sans-serif" font-weight="700" font-size="38" fill="#13284f">TBW</text>

    <g>
      <path d="M466 262H298l-28 25 28 25h168z" fill="#13284f"/>
      <circle cx="466" cy="287" r="22" fill="#c9ced6" stroke="#ffffff" stroke-width="3"/>
      <rect x="458" y="278" width="16" height="18" rx="1" fill="none" stroke="#13284f" stroke-width="2"/>
      <text x="345" y="292" font-family="Poppins, sans-serif" font-weight="600" font-size="13" fill="#ffffff">Finance</text>

      <path d="M733 262h168l28 25-28 25H733z" fill="#13284f"/>
      <circle cx="733" cy="287" r="22" fill="#c9ced6" stroke="#ffffff" stroke-width="3"/>
      <circle cx="733" cy="287" r="8" fill="none" stroke="#13284f" stroke-width="2"/>
      <text x="765" y="292" font-family="Poppins, sans-serif" font-weight="600" font-size="13" fill="#ffffff">Strategy</text>

      <path d="M466 416H298l-28 25 28 25h168z" fill="#13284f"/>
      <circle cx="466" cy="441" r="22" fill="#c9ced6" stroke="#ffffff" stroke-width="3"/>
      <path d="M456 446l10-8 10 8M460 434a3 3 0 1 0 0.1 0M472 434a3 3 0 1 0 0.1 0" fill="none" stroke="#13284f" stroke-width="2"/>
      <text x="315" y="446" font-family="Poppins, sans-serif" font-weight="600" font-size="13" fill="#ffffff">Partnerships</text>

      <path d="M733 416h168l28 25-28 25H733z" fill="#13284f"/>
      <circle cx="733" cy="441" r="22" fill="#c9ced6" stroke="#ffffff" stroke-width="3"/>
      <circle cx="729" cy="444" r="6" fill="none" stroke="#13284f" stroke-width="2"/>
      <circle cx="739" cy="435" r="4" fill="none" stroke="#13284f" stroke-width="2"/>
      <text x="765" y="446" font-family="Poppins, sans-serif" font-weight="600" font-size="13" fill="#ffffff">Operations</text>
    </g>
  </svg>

  <a class="btn btn-green" style="left:527px;top:528px;width:146px;height:30px">Contact Us Today!</a>
</section>

<footer class="section footer">
  <div class="brand" style="left:199px;top:78px">
    <span class="brand-mark" style="background:var(--green)"></span>
    <span class="brand-name" style="font-size:15px;color:var(--white)">TALLOWBROOK</span>
  </div>
  <div class="f-col" style="left:431px">
    <h5>Quick Links</h5>
    <a>Our Approach</a><a>Investment Criteria</a><a>About Us</a><a>Contact Us</a>
  </div>
  <div class="f-col" style="left:613px">
    <h5>Our Team</h5>
    <a style="font-size:12px;color:var(--white)"><span style="color:var(--green)">✆</span> +44(0) 7700-900123</a>
    <span class="btn btn-green" style="position:relative;width:88px;height:28px;margin-top:14px">✉&nbsp; Email Us</span>
  </div>
  <div class="f-col" style="left:819px">
    <h5>Address</h5>
    <div style="display:flex;gap:8px;font-size:9px;line-height:14px;color:#d9e0ec">
      <svg width="10" height="14" viewBox="0 0 10 14"><path d="M5 13S1 8 1 5a4 4 0 0 1 8 0c0 3-4 8-4 8z" fill="#6bb33f"/><circle cx="5" cy="5" r="1.5" fill="#0f2347"/></svg>
      <span>Tallowbrook Wealth Partners Ltd.<br>14 Harbour Court<br>St. Anne<br>Barbados</span>
    </div>
  </div>
  <div class="f-bottom">
    <span>© 2024 <span style="color:var(--green)">Tallowbrook Wealth Partners Ltd.</span> All Rights Reserved &nbsp; | &nbsp; Sitemap &nbsp; | &nbsp; Terms of use &nbsp; | &nbsp; Privacy Policy</span>
    <span class="socials"><i></i><i style="background:var(--green)"></i><i></i><i></i></span>
  </div>
</footer>

</body>
</html>
```